Web design for Money Service Business (uncoded)

We need a very basic website with 5-6 pages. Home page, Services, Transfer(How to use our service), About us, Contact us, FAQ
Our company name is Meridale Exchange. We are a company that deals with currency exchange and international money transfer. We do cash exchange and international money transfers to bank accounts all over the world. We offer highly competitive exchange rates so usually attract customers who transfer money over $10,000. Our niche is with larger sums of money, the design needs to be professional and communicate trust, security and stability.

```html
<!DOCTYPE html>
<html lang="en">
<head>
<meta charset="utf-8">
<title>Meridale Exchange – International Money Transfer</title>
<link rel="stylesheet" href="https://fonts.googleapis.com/css2?family=Jost:wght@300;400;500&family=Open+Sans:wght@400;600;700&display=swap">
<style>
  :root {
    --blue: #1d5586;
    --blue-dark: #174a76;
    --orange: #f9a134;
    --brown: #6a3a10;
    --grey-head: #7a7a7a;
    --grey-text: #9a9a9a;
    --grey-bar: #ebebeb;
    --line: #d6d6d6;
    --white: #ffffff;
  }
  * { margin: 0; padding: 0; box-sizing: border-box; }
  html, body { width: 1200px; height: 1080px; overflow: hidden; background: var(--white); }
  body { position: relative; font-family: "Open Sans", Arial, sans-serif; }

  .site-header { position: absolute; left: 0; top: 0; width: 1200px; height: 52px; background: var(--grey-bar); }
  .brand { position: absolute; left: 200px; top: 13px; display: flex; align-items: center; gap: 6px;
           font-family: "Jost", sans-serif; font-weight: 500; font-size: 22px; color: var(--blue); letter-spacing: .5px; }
  .brand-dot { width: 12px; height: 12px; border-radius: 50%; background: var(--blue); }
  .main-nav { position: absolute; right: 200px; top: 14px; display: flex; align-items: center;
              font-family: "Jost", sans-serif; font-size: 13px; color: #8a8a8a; }
  .main-nav a { color: inherit; text-decoration: none; padding: 0 16px; border-left: 1px solid #d4d4d4; line-height: 14px; }
  .main-nav a:last-child { padding-right: 0; }
  .main-nav a.active { background: var(--orange); color: var(--white); border: 1px solid #e58f22; border-radius: 2px;
                       padding: 5px 13px; margin-right: 14px; }
  .main-nav a.active + a { border-left: none; }

  .hero { position: absolute; left: 0; top: 52px; width: 1200px; height: 422px; background: var(--blue); overflow: hidden; }
  .hero-shape { position: absolute; left: 0; top: 0; }
  .hero-photo { position: absolute; left: 184px; top: 28px; width: 404px; height: 394px;
                background: radial-gradient(ellipse at 50% 35%, #c9a48e 0%, #7b5a4a 35%, #2b3450 70%, #1d2a45 100%);
                border-radius: 180px 180px 0 0; }
  .hero-copy { position: absolute; right: 199px; top: 146px; text-align: right; font-family: "Jost", sans-serif; color: var(--white); }
  .hero-title { font-size: 66px; font-weight: 500; line-height: 62px; letter-spacing: -2px; }
  .hero-title span, .hero-sub span { color: var(--orange); }
  .hero-sub { font-size: 19px; font-weight: 400; line-height: 22px; letter-spacing: -.5px; margin-top: 2px; }
  .hero-text { position: absolute; left: 573px; top: 240px; width: 430px; font-size: 15px; line-height: 16px; color: #cfdbe8; }
  .hero-amount { position: absolute; right: 199px; top: 254px; font-family: "Open Sans", sans-serif; font-weight: 600;
                 font-size: 46px; color: var(--orange); letter-spacing: -2px; }
  .btn { position: absolute; display: flex; align-items: center; justify-content: center;
         font-family: "Open Sans", sans-serif; font-weight: 600; font-size: 17px; border-radius: 2px; letter-spacing: -.5px; }
  .btn-orange { left: 897px; top: 335px; width: 104px; height: 34px; background: var(--orange); color: var(--blue); }
  .btn-blue { left: 200px; top: 684px; width: 105px; height: 35px; background: var(--blue); color: var(--white); }

  .welcome-title { position: absolute; left: 200px; top: 505px; font-family: "Jost", sans-serif; font-weight: 400; font-size: 32px;
                   line-height: 40px; color: var(--grey-head); letter-spacing: -1px; white-space: nowrap; }
  .welcome-title .b { color: var(--blue); }
  .welcome-title .o { color: var(--orange); }
  .welcome-text { position: absolute; left: 200px; top: 548px; width: 800px; font-size: 12.8px; line-height: 17.6px; color: var(--grey-text); }

  .divider { position: absolute; left: 200px; top: 758px; width: 800px; border-top: 1px dashed var(--line); }
  .col-divider { position: absolute; left: 653px; top: 805px; height: 191px; border-left: 1px dashed var(--line); }

  .offer { position: absolute; left: 200px; top: 805px; width: 397px; height: 190px; background: var(--orange);
           border: 3px solid #ececec; }
  .offer-ribbon { position: absolute; left: -9px; top: -6px; }
  .offer-title { position: absolute; left: 80px; top: 18px; font-family: "Jost", sans-serif; font-weight: 400; font-size: 26px;
                 color: var(--brown); letter-spacing: -.5px; line-height: 30px; white-space: nowrap; }
  .offer-rule { position: absolute; left: 81px; right: 12px; top: 54px; border-top: 1px dashed #d9852a; }
  .offer-text { position: absolute; left: 35px; top: 72px; width: 350px; font-size: 12px; line-height: 16px; color: var(--brown); }
  .offer-perks { position: absolute; left: 35px; top: 152px; font-family: "Jost", sans-serif; font-weight: 500; font-size: 15.5px;
                 line-height: 20px; color: var(--white); white-space: nowrap; }
  .offer-perks i { font-style: normal; margin: 0 9px; }

  .news-title { position: absolute; left: 708px; top: 796px; font-family: "Jost", sans-serif; font-weight: 400; font-size: 26px;
                color: var(--orange); letter-spacing: -1px; }
  .news-item { position: absolute; left: 708px; width: 294px; height: 41px; }
  .news-date { position: absolute; left: 2px; top: -2px; font-family: "Jost", sans-serif; color: var(--blue); text-align: center; }
  .news-date b { display: block; font-weight: 400; font-size: 25px; line-height: 24px; }
  .news-date small { display: block; font-size: 14px; line-height: 13px; color: var(--grey-text); }
  .news-card { position: absolute; left: 36px; top: 0; }
  .news-text { position: absolute; left: 54px; top: 7px; width: 232px; font-size: 10.4px; line-height: 14px; color: #7e7e7e; }

  .site-footer { position: absolute; left: 0; top: 1038px; width: 1200px; height: 42px; background: var(--blue); }
  .footer-links { position: absolute; left: 199px; top: 14px; font-family: "Jost", sans-serif; font-size: 11.5px; color: #b6c8da; }
  .footer-links span { margin: 0 6px; }
  .footer-brand { position: absolute; right: 199px; top: 11px; font-family: "Jost", sans-serif; font-weight: 500;
                  font-size: 16px; color: #9fb6cc; }
</style>
</head>
<body>
  <header class="site-header">
    <div class="brand"><span class="brand-dot"></span>Meridale Exchange</div>
    <nav class="main-nav">
      <a class="active" href="#">Home</a>
      <a href="#">Services</a>
      <a href="#">Transfer</a>
      <a href="#">About Us</a>
      <a href="#">Contact Us</a>
      <a href="#">FAQ</a>
    </nav>
  </header>

  <section class="hero">
    <svg class="hero-shape" width="1200" height="422" aria-hidden="true">
      <polygon points="1144,0 1200,0 1200,422 1148,422 1018,208" fill="var(--orange)"/>
    </svg>
    <div class="hero-photo" role="img" aria-label="Photo of a smiling businesswoman in a dark blazer"></div>
    <div class="hero-copy">
      <h1 class="hero-title"><span>WE</span> BELIEVE IN</h1>
      <p class="hero-sub">FAIRNESS AND TRANSPARENCY SO YOU <span>SAVE</span> MONEY</p>
    </div>
    <p class="hero-text">We offer highly competitive exchange rates so usually attract customers who transfer money over</p>
    <div class="hero-amount">$10,000</div>
    <a class="btn btn-orange">Read More</a>
  </section>

  <h2 class="welcome-title">WELCOME TO <span class="b">MERIDALE</span> <span class="o">EXCHANGE</span></h2>
  <p class="welcome-text">Lorem ipsum dolor sit amet, consectetur adipiscing elit. Suspendisse et magna orci. Mauris fringilla magna at interdum ultricies. Phasellus porta ultrices quam, vel convallis tellus fermentum sit amet. Ut a suscipit quam. Phasellus consectetur augue ac ante volutpat, vitae viverra lectus ullamcorper. Cras tempus iaculis ultrices. Mauris vel porta quam, sit amet placerat quam. Suspendisse potenti. Suspendisse vehicula tincidunt tellus, id fringilla odio adipiscing vitae.<br>Pellentesque vel nisi quis enim feugiat scelerisque. Donec ligula tortor, pharetra nec elementum a, dignissim sed felis. Nulla a est erat. nec ante sed dui iaculis auctor at dapibus tellus.</p>
  <a class="btn btn-blue">Read More</a>

  <div class="divider"></div>

  <section class="offer">
    <svg class="offer-ribbon" width="140" height="100" aria-hidden="true">
      <polygon points="0,70 2,90 128,0 100,0" fill="var(--blue)"/>
      <polygon points="100,0 128,0 132,4" fill="var(--blue-dark)"/>
      <text x="14" y="81" transform="rotate(-37 14 81)" font-family="Open Sans, sans-serif" font-size="12.5" fill="#ffffff">Discounts Offer</text>
    </svg>
    <h3 class="offer-title">CURRENCY EXCHANGE</h3>
    <div class="offer-rule"></div>
    <p class="offer-text">Lorem ipsum dolor sit amet, consectetur adipiscing elit. Suspendisse et magna orci. Mauris fringilla magna at interdum ultricies. Phasellus porta ultrices quam, vel convallis tellus fermentum sit amet. Ut a suscipit quam.</p>
    <p class="offer-perks">Best Rates<i>|</i>No Commission<i>|</i>No Bank Fees</p>
  </section>

  <div class="col-divider"></div>

  <section class="news">
    <h3 class="news-title">LATEST NEWS</h3>
    <article class="news-item" style="top:845px">
      <div class="news-date"><b>25</b><small>DEC</small></div>
      <svg class="news-card" width="258" height="41" aria-hidden="true"><polygon points="0,20.5 14,0 258,0 258,41 14,41" fill="var(--grey-bar)" stroke="#dedede"/></svg>
      <p class="news-text">Lorem ipsum dolor sit amet, consectetur adipis cing elit. Suspendisse et magna orci.</p>
    </article>
    <article class="news-item" style="top:901px">
      <div class="news-date"><b>24</b><small>DEC</small></div>
      <svg class="news-card" width="258" height="41" aria-hidden="true"><polygon points="0,20.5 14,0 258,0 258,41 14,41" fill="var(--grey-bar)" stroke="#dedede"/></svg>
      <p class="news-text">Lorem ipsum dolor sit amet, consectetur adipis cing elit. Suspendisse et magna orci.</p>
    </article>
    <article class="news-item" style="top:957px">
      <div class="news-date"><b>23</b><small>DEC</small></div>
      <svg class="news-card" width="258" height="41" aria-hidden="true"><polygon points="0,20.5 14,0 258,0 258,41 14,41" fill="var(--grey-bar)" stroke="#dedede"/></svg>
      <p class="news-text">Lorem ipsum dolor sit amet, consectetur adipis cing elit. Suspendisse et magna orci.</p>
    </article>
  </section>

  <footer class="site-footer">
    <p class="footer-links">Copyright © 2012-2013 Meridale Exchange. All Rights Reserved<span>|</span>Privacy Policy<span>|</span>Terms &amp; Conditions</p>
    <div class="footer-brand">Meridale Exchange</div>
  </footer>
</body>
</html>
```